One page financial canvas needed

I am in the process of developing a financial planning process that uses a one page canvas as a tool for financial education and to explain simple and complex financial strategies to clients. I have the layout and content sorted, just need a hand making it look professional.

It should be a fairly simple project and i have attached a very rough hand drawn canvas showing the desired layout and content. Please feel free to be creative with the design keeping in mind this layout has been chosen to achieve certain outcomes.

Target Market(s)

25-45 Year old Homeowners who are interested in taking better care of the finances

Industry/Entity Type

Financial

Colors

Designer to choose colors to be used in the design.

Requirements
Must have
• very close to the layout in the attached file

```html
<!DOCTYPE html>
<html lang="en">
<head>
<meta charset="utf-8">
<title>Financial Planning Canvas</title>
<link rel="stylesheet" href="https://fonts.googleapis.com/css2?family=PT+Sans:wght@400;700&display=swap">
<style>
  :root {
    --sheet: #ffffff;
    --sheet-shade: #e9e9ea;
    --pill-top: #aab8ee;
    --pill-mid: #6079cf;
    --pill-bottom: #324fa8;
    --pill-edge: #22397e;
    --pill-text: #ffffff;
    --rule: #1d1d1d;
    --frame: #e4e4e4;
    --money-light: #d3d6c4;
    --money-dark: #8b957a;
    --gold-light: #f3b63a;
    --gold-dark: #6a3208;
  }
  * { box-sizing: border-box; margin: 0; padding: 0; }
  html, body { width: 1200px; height: 882px; overflow: hidden; }
  body {
    position: relative;
    font-family: "PT Sans", Arial, sans-serif;
    background: radial-gradient(ellipse 55% 45% at 50% 52%, var(--sheet) 55%, var(--sheet-shade) 100%);
  }
  .rule { position: absolute; background: var(--rule); }
  .rule--v { width: 1.5px; }
  .rule--h { height: 1.5px; }

  .photo {
    position: absolute;
    border: 4px solid var(--frame);
    box-shadow: 0 1px 2px rgba(0,0,0,.15);
  }
  .photo--goals { left: 18px; top: 110px; width: 145px; height: 125px; background: linear-gradient(160deg, #7c8578, #4d5552 60%, #5f8f5a); }
  .photo--income { left: 385px; top: 46px; width: 145px; height: 93px; background: radial-gradient(circle at 55% 50%, #c9c4a4 0 30%, #f7f7f5 60%); }
  .photo--expenses { left: 673px; top: 48px; width: 146px; height: 91px; background: linear-gradient(135deg, #c4b9ae, #e9ecef 55%, #7fa6d6); }
  .photo--fears { left: 908px; top: 14px; width: 143px; height: 89px; background: linear-gradient(120deg, #1c1510, #4b3327 60%, #2a1d16); }
  .photo--frustrations { left: 908px; top: 282px; width: 145px; height: 93px; background: linear-gradient(100deg, #f1f1f1, #d8c7ae 55%, #c9a582); }
  .photo--assets { left: 343px; top: 482px; width: 146px; height: 92px; background: linear-gradient(180deg, #3d78c9, #9ac0e6 45%, #e8e6e0 70%, #6b8c4e); }
  .photo--debt { left: 714px; top: 482px; width: 145px; height: 92px; background: linear-gradient(135deg, #7a5a45, #e8d3a9 50%, #d98a63); }
  .photo--partners { left: 907px; top: 549px; width: 146px; height: 93px; background: radial-gradient(circle, #c98c6a 0 35%, #f2f2f2 75%); }

  .label {
    position: absolute;
    height: 51px;
    border-radius: 26px;
    border: 2px solid var(--pill-edge);
    background:
      linear-gradient(180deg, rgba(255,255,255,.45) 0, rgba(255,255,255,.12) 48%, rgba(255,255,255,0) 50%),
      linear-gradient(180deg, var(--pill-top), var(--pill-mid) 50%, var(--pill-bottom));
    box-shadow: 0 4px 4px rgba(0,0,0,.35);
    color: var(--pill-text);
    font-size: 38px;
    line-height: 48px;
    text-align: center;
    white-space: nowrap;
    letter-spacing: .3px;
    text-shadow: 0 1px 2px rgba(0,0,0,.45);
  }
  .label--goals { left: 16px; top: 246px; width: 136px; }
  .label--income { left: 349px; top: 150px; width: 219px; }
  .label--expenses { left: 636px; top: 150px; width: 220px; }
  .label--fears { left: 906px; top: 113px; width: 133px; }
  .label--cashflow { left: 460px; top: 247px; width: 279px; }
  .label--frustrations { left: 905px; top: 384px; width: 282px; }
  .label--assets { left: 329px; top: 587px; width: 172px; }
  .label--debt { left: 699px; top: 587px; width: 172px; }
  .label--partners { left: 905px; top: 655px; width: 199px; }
  .label--time { left: 84px; top: 814px; width: 111px; }

  .money-hub {
    position: absolute; left: 522px; top: 315px; width: 160px; height: 160px;
    border-radius: 50%;
    background: radial-gradient(circle, var(--money-light) 0, var(--money-dark) 100%);
  }
  .wealth {
    position: absolute; left: 493px; top: 695px; width: 212px; height: 106px;
    border-radius: 106px 106px 0 0;
    background: radial-gradient(circle at 50% 100%, var(--gold-light) 0, #d98a1e 45%, var(--gold-dark) 100%);
    color: #fff; font-size: 40px; line-height: 1; text-align: center; padding-top: 58px;
    text-shadow: 0 1px 3px rgba(0,0,0,.6);
  }
  .clock { position: absolute; left: 12px; top: 807px; width: 60px; height: 60px; }
</style>
</head>
<body>
  <div class="rule rule--v" style="left:599px; top:38px; height:202px;"></div>
  <div class="rule rule--v" style="left:599px; top:496px; height:186px;"></div>
  <div class="rule rule--h" style="left:319px; top:402px; width:189px;"></div>
  <div class="rule rule--h" style="left:693px; top:402px; width:189px;"></div>
  <div class="rule rule--h" style="left:426px; top:801px; width:348px;"></div>

  <div class="photo photo--goals" role="img" aria-label="Woman placing sticky notes on a board"></div>
  <div class="label label--goals">GOALS</div>

  <div class="photo photo--income" role="img" aria-label="Roll of banknotes"></div>
  <div class="label label--income">INCOME</div>

  <div class="photo photo--expenses" role="img" aria-label="Hand working through bills with a calculator"></div>
  <div class="label label--expenses">EXPENSES</div>

  <div class="photo photo--fears" role="img" aria-label="Worried person"></div>
  <div class="label label--fears">FEARS</div>

  <div class="label label--cashflow">CASH FLOW</div>

  <div class="money-hub" role="img" aria-label="Fanned banknotes"></div>

  <div class="photo photo--frustrations" role="img" aria-label="Stressed woman at a computer"></div>
  <div class="label label--frustrations">FRUSTRATIONS</div>

  <div class="photo photo--assets" role="img" aria-label="Family home"></div>
  <div class="label label--assets">ASSETS</div>

  <div class="photo photo--debt" role="img" aria-label="Urgent final notice letters"></div>
  <div class="label label--debt">DEBT</div>

  <div class="photo photo--partners" role="img" aria-label="Hands linked together"></div>
  <div class="label label--partners">PARTNERS</div>

  <div class="wealth" role="img" aria-label="Gold coins and bars">WEALTH</div>

  <svg class="clock" viewBox="0 0 60 60" aria-hidden="true">
    <circle cx="30" cy="30" r="28" fill="#fff" stroke="#111" stroke-width="2"/>
    <line x1="30" y1="30" x2="17" y2="22" stroke="#111" stroke-width="1.5"/>
    <line x1="30" y1="30" x2="44" y2="17" stroke="#111" stroke-width="1"/>
    <line x1="30" y1="30" x2="24" y2="40" stroke="#c22" stroke-width="1"/>
    <circle cx="30" cy="30" r="1.5" fill="#111"/>
  </svg>
  <div class="label label--time">TIME</div>
</body>
</html>
```